Book cover for ebook and Physical book for Mind Clutter Collective

I run a non-profit Mind Clutter Collective and I have a new book that needs a cover. For the physical book, I will need a full wrap. The mission is to help individuals Escape the cycle of restless inner chatter. This book is title is "Escape the cycle of restless inner chatter", and subtitle "Release Your Mind from Clutter." I am open to anything design wise, nothing is set in stone. Oh, MCC is pending Trademark.

Target Market(s)

Typically it's Mom's from 25-40

Industry/Entity Type

Mental Health

Font styles to use
Serif

Colors
f37122
9bcb3b
fbed22
0255a3
e34197

Requirements
Must have
• I do like simplicity, yet vibrant colors.
Nice to have
• The authors are Neil R. Dawkins, and Vera Holmquist. For some inspiration individuals refer to me as the Wonder Healer having reversed five incurable diseases.
Should not have
• The cover shouldn't be too busy.

```html
<!DOCTYPE html>
<html lang="en">
<head>
<meta charset="utf-8">
<title>Escape the Cycle of Restless Inner Chatter — Book Cover</title>
<link rel="stylesheet" href="https://fonts.googleapis.com/css2?family=Bebas+Neue&family=Oswald:wght@400;500;600&display=swap">
<style>
  :root {
    --backdrop: #e7e4df;
    --cover: #efece6;
    --spine: #1f6f93;
    --navy: #1d3a6b;
    --magenta: #8e2a68;
    --rule: #2b8bb8;
    --green: #9bcb3b;
    --orange: #f37122;
    --pink: #e34197;
    --yellow: #fbed22;
    --blue: #0255a3;
    --white: #ffffff;
  }
  html, body {
    margin: 0;
    padding: 0;
    width: 1200px;
    height: 796px;
    overflow: hidden;
    background: var(--backdrop);
  }
  .book-cover {
    position: absolute;
    left: 335px;
    top: 48px;
    width: 530px;
    height: 700px;
    background: var(--cover);
    box-shadow: 0 6px 18px rgba(0,0,0,0.12);
    overflow: hidden;
  }
  .book-cover__spine-edge {
    position: absolute;
    left: 0;
    top: 0;
    width: 10px;
    height: 100%;
    background: var(--spine);
  }
  .title-block {
    position: absolute;
    left: 0;
    top: 0;
    width: 530px;
    height: 230px;
  }
  .title-font {
    font-family: "Bebas Neue", "Oswald", sans-serif;
  }
  .title-tagline {
    position: absolute;
    left: 0;
    top: 228px;
    width: 100%;
    margin: 0;
    text-align: center;
    font-family: "Oswald", sans-serif;
    font-weight: 600;
    font-size: 34px;
    line-height: 1.02;
    color: var(--navy);
    text-transform: uppercase;
  }
  .title-rule {
    position: absolute;
    left: 264px;
    top: 330px;
    width: 2px;
    height: 66px;
    background: var(--rule);
  }
  .subtitle {
    position: absolute;
    left: 0;
    top: 414px;
    width: 100%;
    margin: 0;
    text-align: center;
    font-family: "Oswald", sans-serif;
    font-weight: 500;
    font-size: 20px;
    letter-spacing: 0.5px;
    color: var(--magenta);
    text-transform: uppercase;
  }
  .brain-artwork {
    position: absolute;
    left: 223px;
    top: 532px;
    width: 84px;
    height: 64px;
    border-radius: 50% 50% 45% 45%;
    background: radial-gradient(circle at 40% 45%, #f2a23c 0%, #d84f8e 45%, #3f8fc9 80%, #7bbf4a 100%);
    opacity: 0.85;
  }
  .authors {
    position: absolute;
    left: 0;
    top: 636px;
    width: 100%;
    margin: 0;
    text-align: center;
    font-family: "Oswald", sans-serif;
    font-weight: 500;
    font-size: 12px;
    letter-spacing: 4px;
    color: var(--navy);
    text-transform: uppercase;
  }
</style>
</head>
<body>
  <main class="book-cover">
    <div class="book-cover__spine-edge"></div>

    <svg class="title-block" viewBox="0 0 530 230" aria-label="Escape">
      <defs>
        <clipPath id="band-area">
          <rect x="0" y="0" width="530" height="150"/>
        </clipPath>
      </defs>
      <g class="colour-bands">
        <rect x="80" y="0" width="75" height="150" fill="var(--green)"/>
        <rect x="155" y="0" width="75" height="150" fill="var(--orange)"/>
        <rect x="230" y="0" width="75" height="150" fill="var(--pink)"/>
        <rect x="305" y="0" width="75" height="150" fill="var(--yellow)"/>
        <rect x="380" y="0" width="75" height="150" fill="var(--blue)"/>
      </g>
      <text class="title-font" x="267" y="218" text-anchor="middle" font-size="142"
            textLength="375" lengthAdjust="spacingAndGlyphs" fill="var(--navy)">ESCAPE</text>
      <text class="title-font" x="267" y="218" text-anchor="middle" font-size="142"
            textLength="375" lengthAdjust="spacingAndGlyphs" fill="var(--white)"
            clip-path="url(#band-area)">ESCAPE</text>
    </svg>

    <h1 class="title-tagline">The cycle of restless<br>inner chatter</h1>
    <div class="title-rule"></div>
    <h2 class="subtitle">Release your mind from clutter</h2>
    <div class="brain-artwork" role="img" aria-label="Small colourful mosaic illustration of a brain"></div>
    <p class="authors">Neil R. Dawkins &amp; Vera Holmquist</p>
  </main>
</body>
</html>
```